Family business needs stationery redesign with new logo

Family owned company, established in 1987 wanting a brand 'refresh'. We are an electrical, refrigeration and construction company based in the Barkly Region Northern Territory, Australia. We have a new logo we would like to use which is uploaded along with our current letterhead and email signature. We are also dropping the word 'contractors' so please do not include this on any designs. Please note also, the 'orange' color used in our logo and designs should be Northern Territory red ochre which is as follows:

RGB (Hex): #C75B12
PantoneĀ® 159 C
CMYK: 1 / 74 / 100 / 7

We are needing our stationery redesigned using our new logo. Please include letterheads, business cards, envelopes, and email signatures.

We currently use our business letterheads for quotations, invoices, letters, HR matters, and internal memos.

We also need a separate simplified letterhead for internal paperwork such as employee leave forms, meeting agendas, and meeting minutes etc.
Updates

Reason: Needing more submissions of full package designs. We are wanting all our stationery, including business cards, letterheads, email signatures, envelopes, etc to be cohesive. We also require ALL the information, as supplied on our template letterhead, to be included on the new letterhead designs. including electrical license no.etc Thank you, K&W

Reason: needing more time as work has got in the way of looking over designs. A lot of designs not meeting the brief/criteria.

Industry/Entity Type

Business

Colors
0355a3
f37122

Requirements
Must have
• The 'orange' color used in the designs should be Northern Territory red ochre which is as follows:
• RGB (Hex): #C75B12
• PantoneĀ® 159 C
• CMYK: 1 / 74 / 100 / 7
• ***MUST INCLUDE ALL INFORMATION THAT IS ON OUR CURRENT LETTERHEAD***
Should not have
• Please do not include the word 'contractors'

```html
<!DOCTYPE html>
<html lang="en">
<head>
<meta charset="utf-8">
<title>K&amp;W Business Card</title>
<link rel="stylesheet" href="https://fonts.googleapis.com/css2?family=Exo+2:wght@500;800&family=Roboto+Slab:wght@700&family=Roboto:wght@400;500&display=swap">
<style>
  :root {
    --navy: #1d2e6e;
    --ochre: #e0561a;
    --stripe-blue: #4456a8;
    --card: #ffffff;
    --backdrop: #f8aa6c;
    --ink-grey: #555a63;
    --rule: #c9ccd2;
  }
  * { box-sizing: border-box; margin: 0; padding: 0; }
  html, body { width: 1200px; height: 856px; overflow: hidden; }
  body { background: var(--backdrop); position: relative; font-family: "Roboto", Arial, sans-serif; }

  .card {
    position: absolute;
    width: 560px; height: 320px;
    background: var(--card);
    border-radius: 30px;
    overflow: hidden;
    box-shadow: 0 6px 18px rgba(150, 70, 20, .18);
  }
  .card--front { left: 70px; top: 470px; }
  .card--back  { left: 590px; top: 70px; }

  /* brand lockup */
  .wordmark {
    display: flex; align-items: center; gap: 14px;
    font-family: "Exo 2", Arial, sans-serif; font-weight: 800;
    color: var(--navy); line-height: 1;
  }
  .wordmark__dot { border-radius: 50%; background: var(--ochre); flex: none; }
  .tagline {
    font-family: "Exo 2", Arial, sans-serif; font-weight: 500;
    color: var(--navy); white-space: nowrap;
  }
  .tagline__sep { color: var(--ochre); padding: 0 .35em; }

  /* front */
  .card--front .lockup {
    position: absolute; left: 0; right: 0; top: 96px;
    display: flex; flex-direction: column; align-items: center; gap: 20px;
  }
  .card--front .wordmark { font-size: 84px; }
  .card--front .wordmark__dot { width: 30px; height: 30px; }
  .card--front .tagline { font-size: 21px; }
  .edge-marks { position: absolute; width: 10px; }
  .edge-marks--left { left: 0; top: 150px; }
  .edge-marks--right { right: 0; top: 44px; }
  .edge-marks span { display: block; height: 38px; }
  .edge-marks .mark-ochre { background: var(--ochre); }
  .edge-marks .mark-blue { background: var(--stripe-blue); margin-top: 8px; }

  /* back */
  .card--back .lockup {
    position: absolute; left: 28px; top: 112px; width: 250px;
    display: flex; flex-direction: column; align-items: center; gap: 14px;
  }
  .card--back .wordmark { font-size: 48px; gap: 10px; }
  .card--back .wordmark__dot { width: 18px; height: 18px; }
  .card--back .tagline { font-size: 12px; }
  .divider { position: absolute; left: 290px; top: 76px; width: 1px; height: 134px; background: var(--rule); }

  .contact { position: absolute; left: 308px; top: 74px; right: 16px; }
  .contact__name { font-family: "Roboto Slab", Georgia, serif; font-weight: 700; font-size: 18px; line-height: 22px; color: var(--ochre); }
  .contact__role { font-family: "Roboto Slab", Georgia, serif; font-weight: 700; font-size: 11px; line-height: 14px; color: var(--navy); margin-bottom: 8px; }
  .contact__list { list-style: none; }
  .contact__list li {
    display: flex; align-items: center; gap: 7px;
    font-size: 11px; color: var(--ink-grey); line-height: 19px; white-space: nowrap;
  }
  .contact__list svg { width: 11px; height: 11px; flex: none; }

  .base-band { position: absolute; left: 0; right: 0; bottom: 0; height: 10px; display: flex; }
  .base-band .band-ochre { flex: 1; background: var(--ochre); }
  .base-band .band-gap { width: 8px; background: var(--card); }
  .base-band .band-blue { width: 96px; background: var(--stripe-blue); }
</style>
</head>
<body>

<section class="card card--front" aria-label="Business card front">
  <div class="edge-marks edge-marks--left"><span class="mark-ochre"></span><span class="mark-blue"></span></div>
  <div class="edge-marks edge-marks--right"><span class="mark-ochre"></span><span class="mark-blue"></span></div>
  <div class="lockup">
    <div class="wordmark"><span class="wordmark__dot"></span>K&amp;W</div>
    <p class="tagline">Electrical<span class="tagline__sep">|</span>Refrigeration<span class="tagline__sep">|</span>Building Services</p>
  </div>
</section>

<section class="card card--back" aria-label="Business card back">
  <div class="lockup">
    <div class="wordmark"><span class="wordmark__dot"></span>K&amp;W</div>
    <p class="tagline">Electrical<span class="tagline__sep">|</span>Refrigeration<span class="tagline__sep">|</span>Building Services</p>
  </div>
  <div class="divider"></div>
  <div class="contact">
    <p class="contact__name">Dale Morrison</p>
    <p class="contact__role">President</p>
    <ul class="contact__list">
      <li><svg viewBox="0 0 12 12"><circle cx="6" cy="6" r="6" fill="#e0561a"/><path d="M6 2.6a2.2 2.2 0 0 0-2.2 2.2C3.8 6.5 6 9.4 6 9.4s2.2-2.9 2.2-4.6A2.2 2.2 0 0 0 6 2.6z" fill="#fff"/><circle cx="6" cy="4.8" r=".8" fill="#e0561a"/></svg>PO Box 214, Tennant Creek, NT 0860</li>
      <li><svg viewBox="0 0 12 12"><circle cx="6" cy="6" r="6" fill="#e0561a"/><rect x="3" y="4" width="6" height="4" rx=".6" fill="#fff"/></svg>1-800-555-0142</li>
      <li><svg viewBox="0 0 12 12"><circle cx="6" cy="6" r="6" fill="#e0561a"/><path d="M4 3.2l1.2 1.4-.6.8c.4.9 1.1 1.6 2 2l.8-.6L8.8 8l-.7 1C5.6 9 3 6.4 3 3.9z" fill="#fff"/></svg>308-555-0178</li>
      <li><svg viewBox="0 0 12 12"><circle cx="6" cy="6" r="6" fill="#e0561a"/><rect x="3" y="3.8" width="6" height="4.4" rx=".5" fill="#fff"/><path d="M3.2 4.2L6 6.3l2.8-2.1" stroke="#e0561a" stroke-width=".7" fill="none"/></svg>dale@kwbuildingservices.com</li>
      <li><svg viewBox="0 0 12 12"><circle cx="6" cy="6" r="6" fill="#e0561a"/><circle cx="6" cy="6" r="3" fill="none" stroke="#fff" stroke-width=".8"/><path d="M3 6h6M6 3v6" stroke="#fff" stroke-width=".7"/></svg>www.kwbuildingservices.com</li>
    </ul>
  </div>
  <div class="base-band"><span class="band-ochre"></span><span class="band-gap"></span><span class="band-blue"></span></div>
</section>

</body>
</html>
```